Fernwick Digital Marketing Agency Website Design. I need a new website for my digital marketing agency. It needs to be FAST and easy to use. I want to be able to add videos to the main homepage like this page: https://www.lumatreeweb.example/search-marketing/cleveland-ohio-seo-companyI'd like to have the request quote tab on the top right side as well as my number above it. The following website is my favorite overall: http://www.vantorelgroup.example/ I'd love to copy something like that.

***** Website I want to copy: http://www.vantorelgroup.example/services/ ******
Updates

This needs to be a Wordpress website. Sorry for any confusion as this is the first time using MakerQuill. I need the homepage as described as well as a Services Page and Contact Us page. Services page should be simply yet creative with a spot for me to insert up to 8 services.

Target Market(s)

Business owners

Industry/Entity Type

Digital Marketing

Coding

Coded - Design and coding required

Number of Pages Required

3 page

Font styles to use
Other font styles liked:
• Oswald

Colors

Designer to choose colors to be used in the design.

Requirements
Must have
• I need to have a nice design/template to work off of in Wordpress. It needs to be bright and vibrant yet elegant in design.
Nice to have
• CTA at the top right as well as a place for the phone number. http://www.vantorelgroup.example/services/

```html
<!DOCTYPE html>
<html lang="en">
<head>
<meta charset="utf-8">
<title>Fernwick Digital Marketing Company</title>
<link rel="stylesheet" href="https://fonts.googleapis.com/css2?family=Source+Sans+Pro:wght@400;700&family=Roboto+Slab:wght@300&family=Tinos&family=Montserrat:wght@700&display=swap">
<style>
  :root {
    --white: #ffffff;
    --ink: #222222;
    --muted: #777777;
    --rule: #e4e4e4;
    --brand-orange: #f7931e;
    --cta-gold: #eeab4c;
    --hero-dark: #231d17;
    --hero-mid: #3a3129;
    --hero-text: #ffffff;
  }
  * { box-sizing: border-box; margin: 0; padding: 0; }
  html, body { width: 1200px; height: 604px; overflow: hidden; background: var(--white); }
  body { position: relative; font-family: "Source Sans Pro", Arial, sans-serif; color: var(--ink); }

  .top-bar {
    position: absolute; left: 0; top: 0; width: 1200px; height: 32px;
    border-top: 3px solid #c8c8c8; border-bottom: 1px solid var(--rule);
  }
  .top-bar__cell {
    position: absolute; top: 0; height: 28px; display: flex; align-items: center;
    font-size: 11px; color: var(--muted);
    border-left: 1px solid var(--rule); border-right: 1px solid var(--rule);
  }
  .top-bar__site { left: 144px; width: 120px; padding-left: 10px; }
  .top-bar__phone { left: 886px; width: 103px; justify-content: center; }
  .top-bar__social { left: 988px; width: 67px; justify-content: center; gap: 12px; border-left: none; }
  .social-dot { width: 9px; height: 9px; border-radius: 50%; background: var(--ink); }

  .site-header { position: absolute; left: 0; top: 32px; width: 1200px; height: 66px; }
  .site-header__name {
    position: absolute; left: 144px; top: 23px;
    font-weight: 700; font-size: 18px; color: var(--brand-orange); letter-spacing: 0.1px;
  }
  .main-nav { position: absolute; right: 155px; top: 25px; display: flex; gap: 26px; }
  .main-nav a { font-family: "Tinos", "Times New Roman", serif; font-size: 12px; color: var(--ink); text-decoration: none; }

  .hero { position: absolute; left: 0; top: 98px; width: 1200px; height: 506px; }
  .hero__backdrop {
    position: absolute; inset: 0;
    background: radial-gradient(ellipse at 50% 40%, var(--hero-mid) 0%, var(--hero-dark) 75%);
  }
  .hero__content { position: absolute; inset: 0; text-align: center; color: var(--hero-text); font-family: "Roboto Slab", Georgia, serif; font-weight: 300; }
  .hero__title { position: absolute; left: 0; right: 0; top: 102px; font-size: 66px; line-height: 1; font-weight: 300; }
  .hero__lead { position: absolute; left: 0; right: 0; top: 216px; font-size: 32px; line-height: 40px; font-weight: 300; }
  .hero__tag { position: absolute; left: 0; right: 0; top: 314px; font-size: 32px; line-height: 40px; font-weight: 300; }
  .hero__cta {
    position: absolute; left: 506px; top: 369px; width: 185px; height: 42px;
    border-radius: 21px; background: var(--cta-gold); color: var(--white);
    font-family: "Montserrat", Arial, sans-serif; font-weight: 700; font-size: 8.5px; letter-spacing: 0.9px;
    display: flex; align-items: center; justify-content: center; text-decoration: none;
  }
</style>
</head>
<body>
  <div class="top-bar">
    <div class="top-bar__cell top-bar__site">www.fernwick.example/</div>
    <div class="top-bar__cell top-bar__phone">Call: 555-014-2290</div>
    <div class="top-bar__cell top-bar__social" aria-label="Social links">
      <span class="social-dot"></span><span class="social-dot"></span>
    </div>
  </div>

  <header class="site-header">
    <div class="site-header__name">FERNWICK DIGITAL MARKETING COMPANY</div>
    <nav class="main-nav">
      <a href="#">Home</a>
      <a href="#">Services</a>
      <a href="#">Blog</a>
      <a href="#">Contact us</a>
      <a href="#">FAQ</a>
    </nav>
  </header>

  <section class="hero">
    <div class="hero__backdrop" role="img" aria-label="Dark overhead photo of a desk with hands holding a pen over charts, a coffee cup, a laptop and a calendar"></div>
    <div class="hero__content">
      <h1 class="hero__title">GROW</h1>
      <p class="hero__lead">THIS IS ALL ABOUT YOUR COMPANY<br>GROWING ONLINE.</p>
      <p class="hero__tag">END OF STORY.</p>
      <a class="hero__cta" href="#">GROW MY COMPANY NOW</a>
    </div>
  </section>
</body>
</html>
```